Eye catching Stationary Design

Healthcare consultant firm looking for stationary design ( letterhead, envelope and business cards) That’s professional, classy and eye catching . The design should incorporate the logo and the colors of the logo in its design. You can see the logo on our website at www crestmore advisory. net.

```html
<!DOCTYPE html>
<html lang="en">
<head>
<meta charset="utf-8">
<title>Crestmore Advisory Stationery</title>
<link href="https://fonts.googleapis.com/css2?family=Cinzel:wght@400;600&family=Open+Sans:wght@400;600;700&family=Great+Vibes&display=swap" rel="stylesheet">
<style>
:root{
  --bg:#dedede;
  --paper:#f0eff0;
  --navy:#0e4f98;
  --deep:#174280;
  --sky:#2f9acb;
  --ink:#3c3c3c;
  --rule:#9a9a9a;
}
*{margin:0;padding:0;box-sizing:border-box}
html,body{width:1200px;height:1037px;overflow:hidden;background:var(--bg)}
body{position:relative;font-family:'Open Sans',sans-serif;color:var(--ink)}
.sheet{position:absolute;background:var(--paper);overflow:hidden}
.brand{font-family:'Cinzel',serif;font-weight:600;color:var(--navy);text-align:center;line-height:1}
.tagname{font-family:'Cinzel',serif;color:#222;text-align:center;white-space:nowrap}
.wave{position:absolute;left:0;bottom:0;width:100%}
.contact{position:absolute;font-size:6px;line-height:7.4px;color:#555}
.contact .ico{color:var(--navy);margin-right:3px}
.divider{position:absolute;width:1px;background:#888}

/* letterhead */
.letterhead{left:59px;top:167px;width:374px;height:525px}
.letterhead .brand{position:absolute;top:27px;width:100%;font-size:17px}
.letterhead .tagname{position:absolute;top:52px;width:100%;font-size:6.4px}
.letterhead .rule{position:absolute;top:55px;height:1px;background:var(--rule)}
.letter{position:absolute;left:40px;top:114px;width:253px;font-size:5.8px;line-height:8.8px;color:#444}
.letter p{margin-bottom:8.6px;text-align:justify}
.letter .date{margin-bottom:9px}
.letter .sign{font-family:'Great Vibes',cursive;font-size:12px;color:#222;margin-top:-5px}
.letter .gap{margin-bottom:17px}

/* folder */
.folder{left:474px;top:130px;width:441px;height:561px}
.folder .spine{position:absolute;top:0;bottom:0;width:1px;background:rgba(0,0,0,.12)}
.folder .brand{position:absolute;top:43px;width:100%;font-size:25px}
.folder .tagname{position:absolute;top:83px;width:100%;font-size:9.6px}
.folder .bigname{position:absolute;top:195px;left:0;width:100%;text-align:center;font-family:'Cinzel',serif;font-weight:600;font-size:58px;color:var(--sky);line-height:1}
.folder .tagline{position:absolute;top:499px;width:100%;text-align:center;color:#fff;font-size:11.6px;letter-spacing:.3px}

/* cards */
.card-front{left:953px;top:289px;width:188px;height:107px}
.card-front .brand{position:absolute;top:16px;left:12px;width:82px;font-size:8px}
.card-front .tagname{position:absolute;top:31px;left:12px;width:82px;font-size:3.4px}
.card-front .contact{left:18px;top:63px;font-size:4px;line-height:5.2px;color:#e3ecf6}
.card-front .person{position:absolute;right:18px;top:81px;text-align:right;color:#fff}
.card-front .person .nm{font-family:'Cinzel',serif;font-size:6.2px}
.card-front .person .role{font-size:3.8px;color:#d7e2f0}
.card-back{left:953px;top:426px;width:188px;height:107px;background:radial-gradient(ellipse at 50% 40%,#2d66b0 0%,#1b4f98 55%,#17407f 100%)}
.card-back .brand{position:absolute;top:37px;width:100%;color:#fff;font-size:12px}
.card-back .tagname{position:absolute;top:53px;width:100%;color:#e6edf6;font-size:6.4px}
.card-back .web{position:absolute;top:89px;width:100%;text-align:center;color:#e6edf6;font-size:4px}

/* envelopes */
.env-front{left:187px;top:730px;width:390px;height:176px}
.env-front .brand{position:absolute;top:26px;left:28px;width:90px;font-size:12px}
.env-front .tagname{position:absolute;top:45px;left:28px;width:90px;font-size:4.8px}
.env-back{left:623px;top:730px;width:390px;height:176px}
.env-back .flap{position:absolute;left:0;top:0}
.env-back .brand{position:absolute;top:20px;width:100%;color:#fff;font-size:13px}
.env-back .edge{position:absolute;top:50px;bottom:6px;width:1px;background:#cfcfcf}
</style>
</head>
<body>

<!-- Letterhead -->
<section class="sheet letterhead">
  <div class="brand">Crestmore</div>
  <div class="rule" style="left:29px;width:95px"></div>
  <div class="rule" style="left:250px;width:95px"></div>
  <div class="tagname">Crestmore Advisory LLC</div>
  <div class="letter">
    <p class="date">01 January 2050</p>
    <p><strong style="color:#222">Company (Pvt) Ltd.</strong><br>PO Box 3355 Mainville St<br>Sample City Country 3355</p>
    <p style="margin-top:15px">Dear Helen Marsh,</p>
    <p>Lorem ipsum dolor sit amet, consectetuer adipiscing elit, sed diam nonummy nibh euismod tincidunt ut laoreet dolore magna aliquam erat volutpat. Ut wisi enim ad minim veniam, quis nostrud exerci tation ullamcorper suscipit lobortis nisl ut aliquip ex ea commodo consequat. Duis dolore te feugait nulla facilisi. Nam liber tempor cum soluta nobis eleifend option congue nihil imperdiet doming id quod mazim placerat facer possim assum. Lorem ipsum dolor sit amet, consectetuer adipiscing elit, sed diam nonummy nibh euismod tincidunt ut laoreet dolore magna aliquam erat volutpat. Ut wisi enim ad minim veniam, quis nostrud exerci tation ullamcorper suscipit lobortis nisl ut aliquip ex ea commodo consequat.</p>
    <p>Consectetuer adipiscing elit, sed diam nonummy nibh euismod tincidunt ut laoreet dolore magna aliquam erat volutpat. Ut wisi enim ad minim veniam, quis nostrud exerci tation ullamcorper suscipit lobortis nisl ut aliquip ex ea commodo consequat. Consectetuer adipiscing elit, sed diam nonummy nibh euismod tincidunt ut laoreet dolore magna aliquam erat volutpat. Ut wisi enim ad minim veniam, quis nostrud exerci tation ullamcorper suscipit lobortis nisl ut aliquip ex ea commodo consequat.</p>
    <p class="gap">Consectetuer adipiscing elit, sed diam nonummy nibh euismod tincidunt ut laoreet dolore magna aliquam erat volutpat. Ut wisi enim ad minim veniam, quis nostrud exerci tation ullamcorper suscipit lobortis nisl ut aliquip ex ea commodo consequat. Consectetuer adipiscing elit, sed diam nonummy nibh euismod tincidunt ut laoreet dolore magna aliquam erat volutpat. Ut wisi enim ad minim veniam, quis nostrud exerci tation ullamcorper suscipit lobortis nisl ut aliquip ex ea commodo consequat.</p>
    <p style="margin-bottom:4px">Sincerely Yours</p>
    <p class="sign">Martin Ellis Crane</p>
  </div>
  <div class="contact" style="left:32px;top:478px"><span class="ico">&#9990;</span>(555) 214-0187<br><span class="ico">&#9993;</span>info@CrestmoreAdvisory.net</div>
  <div class="divider" style="left:131px;top:477px;height:16px"></div>
  <div class="contact" style="left:138px;top:478px">18 Larkfield Rd Suite 4, Northvale<br>NV 20410, USA</div>
  <div class="contact" style="right:32px;top:486px">www.<strong>CrestmoreAdvisory</strong>.net</div>
  <svg class="wave" width="374" height="22" viewBox="0 0 374 22" preserveAspectRatio="none" aria-hidden="true">
    <path d="M0 9 Q180 -2 374 15 L374 16 Q180 2 0 12Z" fill="var(--sky)"/>
    <path d="M0 13 Q180 4 374 18 L374 22 L0 22Z" fill="var(--navy)"/>
  </svg>
</section>

<!-- Presentation folder -->
<section class="sheet folder">
  <svg style="position:absolute;left:0;top:0" width="441" height="561" viewBox="0 0 441 561" aria-hidden="true">
    <defs>
      <linearGradient id="folderBlue" x1="0" y1="0" x2="0" y2="1">
        <stop offset="0" stop-color="#2360a8"/>
        <stop offset="1" stop-color="#14427f"/>
      </linearGradient>
    </defs>
    <path d="M0 302 Q220 272 441 300 L441 561 L0 561Z" fill="url(#folderBlue)"/>
  </svg>
  <div class="spine" style="left:19px"></div>
  <div class="spine" style="left:34px"></div>
  <div class="brand">Crestmore</div>
  <div class="tagname">Crestmore Advisory LLC</div>
  <div class="bigname">Crestmore</div>
  <div class="tagline">ADVANCING HEALTHCARE OPERATIONS</div>
</section>

<!-- Business card front -->
<section class="sheet card-front">
  <svg class="wave" width="188" height="56" viewBox="0 0 188 56" preserveAspectRatio="none" aria-hidden="true">
    <path d="M0 3 Q100 -4 188 12 L188 13 Q100 0 0 5Z" fill="var(--sky)"/>
    <path d="M0 6 Q100 1 188 15 L188 56 L0 56Z" fill="var(--navy)"/>
  </svg>
  <div class="brand">Crestmore</div>
  <div class="tagname">Crestmore Advisory LLC</div>
  <div class="contact">18 Larkfield Rd Suite 4, Northvale<br>NV 20410, USA<br><span style="display:block;height:4px"></span>&#9990; (555) 214-0187<br>&#9993; info@CrestmoreAdvisory.net<br>&#9679; www.CrestmoreAdvisory.net</div>
  <div class="person"><div class="nm">Daniel Ashford</div><div class="role">Managing Director</div></div>
</section>

<!-- Business card back -->
<section class="sheet card-back">
  <div class="brand">Crestmore</div>
  <div class="tagname">Crestmore Advisory LLC</div>
  <div class="web">www.<strong>CrestmoreAdvisory</strong>.net</div>
</section>

<!-- Envelope front -->
<section class="sheet env-front">
  <div class="brand">Crestmore</div>
  <div class="tagname">Crestmore Advisory LLC</div>
  <div class="contact" style="left:30px;top:127px;font-size:5.6px;line-height:7.2px"><span class="ico">&#9990;</span>(555) 214-0187<br><span class="ico">&#9993;</span>info@CrestmoreAdvisory.net<br><span class="ico">&#9679;</span>www.CrestmoreAdvisory.net</div>
  <div class="divider" style="left:123px;top:126px;height:22px"></div>
  <div class="contact" style="left:133px;top:127px;font-size:5.6px;line-height:7.2px">Crestmore Advisory (CA)<br>18 Larkfield Rd Suite 4, Northvale<br>NV 20410, USA</div>
  <svg class="wave" width="390" height="20" viewBox="0 0 390 20" preserveAspectRatio="none" aria-hidden="true">
    <path d="M0 6 Q200 -3 390 16 L390 17 Q200 0 0 9Z" fill="var(--sky)"/>
    <path d="M0 10 Q200 2 390 19 L390 20 L0 20Z" fill="var(--navy)"/>
  </svg>
</section>

<!-- Envelope back -->
<section class="sheet env-back">
  <svg class="flap" width="390" height="66" viewBox="0 0 390 66" aria-hidden="true">
    <path d="M0 0 L390 0 L380 52 Q378 62 366 63 L24 63 Q12 62 10 52Z" fill="var(--navy)"/>
  </svg>
  <div class="edge" style="left:6px"></div>
  <div class="edge" style="right:6px"></div>
  <div class="brand">Crestmore</div>
</section>

</body>
</html>
```